Verlotti Magician

I want the business card for my business to give to people who watch that later I will be employed to show magic here is my website http://www.verlottimagicien.net/I want the interesting design , i am very opened for formal and informal, I watch a lot of design so don't stick to the common shape and form but i hope it can also be produced the thing to write on will be the same as in picture that i will upload , i also will upload the logo for you that so can be easy to useDenis CostilleMagicianMAGICIAN VERLOTTI 17 rue des Tilleuls - 25870 MONTCLAREL contact@verlottimagicien.net tel. 0384 519 467 tel. 0672 904 153

```html
<!DOCTYPE html>
<html lang="fr">
<head>
<meta charset="utf-8">
<title>Verlotti Magician – Business Card</title>
<link rel="stylesheet" href="https://fonts.googleapis.com/css2?family=Jost:wght@300;400;500&display=swap">
<style>
  :root {
    --stage: #3b3c3f;
    --card: #ffffff;
    --ink: #141414;
    --red: #d13236;
    --muted: #2a2a2a;
  }
  * { box-sizing: border-box; margin: 0; padding: 0; }
  html, body { width: 1200px; height: 900px; overflow: hidden; }
  body {
    background: var(--stage);
    font-family: "Jost", sans-serif;
    color: var(--ink);
    position: relative;
  }
  .card {
    position: absolute;
    width: 640px;
    height: 366px;
    background: var(--card);
    border-radius: 26px;
    overflow: hidden;
  }
  .card--back { left: 60px; top: 50px; }
  .card--front { left: 500px; top: 480px; }

  /* back side */
  .back-portrait {
    position: absolute;
    left: 220px; top: 44px;
    width: 200px; height: 220px;
    background: linear-gradient(180deg, #1a1a1a 0%, #0d0d0d 100%);
    border-radius: 90px 90px 14px 14px;
  }
  .wordmark {
    font-weight: 300;
    letter-spacing: 0.06em;
    color: var(--ink);
    line-height: 1;
  }
  .card--back .wordmark {
    position: absolute;
    left: 0; right: 0; top: 282px;
    text-align: center;
    font-size: 46px;
  }

  /* front side */
  .front-portrait {
    position: absolute;
    left: 28px; top: 70px;
    width: 300px; height: 296px;
    background: linear-gradient(180deg, #1a1a1a 0%, #0c0c0c 100%);
    border-radius: 120px 120px 0 0;
  }
  .front-info {
    position: absolute;
    left: 352px; top: 34px;
    width: 270px;
  }
  .card--front .wordmark { font-size: 40px; }
  .holder-name {
    margin-top: 26px;
    font-size: 25px;
    font-weight: 400;
    color: var(--red);
    letter-spacing: 0.01em;
  }
  .holder-role {
    margin-top: 4px;
    font-size: 15px;
    font-weight: 500;
    letter-spacing: 0.04em;
  }
  .divider {
    margin-top: 8px;
    width: 140px;
    height: 1.5px;
    background: var(--red);
  }
  .contacts { list-style: none; margin-top: 10px; }
  .contacts li {
    display: flex;
    align-items: center;
    gap: 9px;
    font-size: 15px;
    font-weight: 400;
    color: var(--muted);
    line-height: 23px;
  }
  .contacts svg { width: 13px; height: 13px; fill: var(--red); flex: none; }
  .address-band {
    position: absolute;
    left: 300px; right: 0; bottom: 0;
    height: 68px;
    background: var(--red);
    color: #fff;
    padding: 12px 0 0 40px;
    font-size: 15px;
    line-height: 21px;
    letter-spacing: 0.02em;
    clip-path: polygon(4% 0, 100% 0, 100% 100%, 0 100%);
  }
</style>
</head>
<body>

<section class="card card--back">
  <div class="back-portrait" role="img" aria-label="Black ink illustration of the magician holding a playing card"></div>
  <div class="wordmark">VERLOTTI</div>
</section>

<section class="card card--front">
  <div class="front-portrait" role="img" aria-label="Black ink illustration of the magician in a jacket holding a playing card"></div>

  <div class="front-info">
    <div class="wordmark">VERLOTTI</div>
    <h1 class="holder-name">HUGO MARSENAC</h1>
    <p class="holder-role">MAGICIAN</p>
    <div class="divider"></div>
    <ul class="contacts">
      <li><svg viewBox="0 0 24 24"><path d="M6.6 10.8a15 15 0 0 0 6.6 6.6l2.2-2.2c.3-.3.7-.4 1-.2 1.1.4 2.3.6 3.6.6.6 0 1 .4 1 1V20c0 .6-.4 1-1 1A17 17 0 0 1 3 4c0-.6.4-1 1-1h3.5c.6 0 1 .4 1 1 0 1.3.2 2.5.6 3.6.1.3 0 .7-.2 1z"/></svg>0384 519 467</li>
      <li><svg viewBox="0 0 24 24"><path d="M3 9c3-4 15-4 18 0l-2 3-4-1V8.5H9V11l-4 1zM6 13h12l2 7H4zm6 2a2 2 0 1 0 0 4 2 2 0 0 0 0-4z"/></svg>0672 904 153</li>
      <li><svg viewBox="0 0 24 24"><path d="M2 5h20v14H2zm2 2v.4l8 5.3 8-5.3V7z"/></svg>contact@verlottimagicien.net</li>
      <li><svg viewBox="0 0 24 24"><path d="M12 2a10 10 0 1 0 0 20 10 10 0 0 0 0-20zm-1 17.9A8 8 0 0 1 4.2 10l4.8 4.8v1a2 2 0 0 0 2 2zm6.9-2.5A2 2 0 0 0 16 16h-1v-3a1 1 0 0 0-1-1H8v-2h2a1 1 0 0 0 1-1V7h2a2 2 0 0 0 2-2v-.4a8 8 0 0 1 2.9 12.8z"/></svg>www.verlottimagicien.net</li>
    </ul>
  </div>

  <div class="address-band">
    <p>MAGICIAN VERLOTTI</p>
    <p>17 rue des Tilleuls - 25870 MONTCLAREL</p>
  </div>
</section>

</body>
</html>
```